Old Scholl Hip Hop Party Design

I need a flyer which shows some old stuff from the 80s, 90s, Hip Hop and RnB
the party is called "Midnight Velvet Groove" its every week on a tuesday
We are a club so the style should be modern and stylisch, i put some samples from old flyers and our logo attached

Bar / Club Party Scene

School

```html
<!DOCTYPE html>
<html lang="en">
<head>
<meta charset="UTF-8">
<title>Midnight Velvet Groove – Weekly Party Flyer</title>
<link rel="stylesheet" href="https://fonts.googleapis.com/css2?family=Oswald:wght@300;400;700&family=Roboto+Condensed:wght@400;700&display=swap">
<style>
  :root {
    --backdrop: #c9c9c9;
    --paper-light: #fbefb4;
    --paper-mid: #f1d56e;
    --paper-deep: #ddb43f;
    --silver-light: #f2f2f2;
    --silver-dark: #b9b9b9;
    --ink: #141414;
    --radio-gold: #c9a843;
    --radio-steel: #8f8a78;
  }
  * { box-sizing: border-box; margin: 0; padding: 0; }
  html, body {
    width: 1200px; height: 900px; overflow: hidden;
    background: var(--backdrop);
  }
  .flyer {
    position: absolute; left: 297px; top: 30px;
    width: 606px; height: 840px; overflow: hidden;
    background:
      radial-gradient(ellipse at 70% 75%, var(--paper-light) 0%, var(--paper-mid) 45%, var(--paper-deep) 100%);
    box-shadow: 0 2px 6px rgba(0,0,0,.2);
  }
  .flyer__corner {
    position: absolute; left: 0; top: 0; width: 280px; height: 262px;
  }
  .brand {
    position: absolute; left: 24px; top: 30px; width: 170px;
    display: flex; flex-direction: column; align-items: center; gap: 8px;
    font-family: "Roboto Condensed", sans-serif; color: var(--ink);
  }
  .brand__dot {
    width: 26px; height: 26px; border-radius: 50%; background: var(--ink);
  }
  .brand__name {
    font-size: 24px; font-weight: 700; letter-spacing: 1px; text-transform: uppercase;
  }
  .brand__place {
    font-size: 9px; font-weight: 700; letter-spacing: 8px; text-transform: uppercase;
  }
  .headline {
    position: absolute; right: 28px; top: 118px;
    font-family: "Oswald", sans-serif; color: var(--ink);
    text-align: right; text-transform: uppercase; line-height: .9;
  }
  .headline span { display: block; }
  .headline__light { font-weight: 300; font-size: 100px; letter-spacing: -1px; }
  .headline__mid { font-weight: 400; font-size: 128px; letter-spacing: -2px; }
  .headline__bold { font-weight: 700; font-size: 158px; letter-spacing: -3px; }
  .boombox {
    position: absolute; left: 236px; top: 500px; width: 344px; height: 264px;
    border-radius: 6px;
    background: linear-gradient(160deg, var(--radio-gold) 0%, var(--radio-steel) 60%, var(--radio-gold) 100%);
  }
  .schedule {
    position: absolute; left: 26px; top: 560px;
    font-family: "Roboto Condensed", sans-serif; color: var(--ink);
    text-transform: uppercase; line-height: .98;
  }
  .schedule__line { display: block; font-size: 41px; font-weight: 400; letter-spacing: -1px; }
  .schedule__day { display: block; font-size: 44px; font-weight: 700; letter-spacing: -1px; }
  .schedule__web {
    display: block; margin-top: 4px;
    font-size: 19px; font-weight: 400; text-transform: none;
  }
</style>
</head>
<body>
  <section class="flyer">
    <svg class="flyer__corner" viewBox="0 0 280 262" aria-hidden="true">
      <defs>
        <linearGradient id="silver" x1="0" y1="0" x2="1" y2="1">
          <stop offset="0" stop-color="var(--silver-light)"/>
          <stop offset="1" stop-color="var(--silver-dark)"/>
        </linearGradient>
      </defs>
      <polygon fill="url(#silver)"
        points="0,0 280,0 268,14 262,30 248,44 240,62 226,78 214,96 200,112 190,130 178,146 162,160 150,178 132,190 118,204 98,214 82,228 62,236 44,246 22,250 0,262"/>
    </svg>

    <div class="brand">
      <div class="brand__dot"></div>
      <div class="brand__name">Cobalt Hall</div>
      <div class="brand__place">Lakeside</div>
    </div>

    <h1 class="headline">
      <span class="headline__light">Midnight</span>
      <span class="headline__mid">Velvet</span>
      <span class="headline__bold">Groove</span>
    </h1>

    <div class="boombox" role="img" aria-label="Photo of a worn 1980s gold and silver boombox stereo"></div>

    <p class="schedule">
      <span class="schedule__line">Every</span>
      <span class="schedule__line">Week</span>
      <span class="schedule__line">On a</span>
      <span class="schedule__day">Tuesday</span>
      <span class="schedule__web">www.cobalthall-club.com</span>
    </p>
  </section>
</body>
</html>
```